Create a flyer for our party getaway to Ibiza.

'The Velvet Ibiza Getaway'

Friday 14th July - Monday 17th July

DJ Korvex & DJ Tamblin brings together a jam-packed weekend schedule full of the best urban parties in Ibiza.

What's included?

4 Nights Of Entertainment
6 Parties In Total
1 Boat Party
1 Pool Party
2 Superclub Parties
1 Indoor Water Party
Bottomless Drinks (Boat Party Only)
An unbelievable experience
1 unbeatable price.

All this for 140€ (you save 50€ when you book with us)

Tickets avaialble from Ticketmoor & Queldrix

Target Market(s)

holiday goers

Industry/Entity Type

party, events, club, hip hop

Requirements
Must have
• good vibes
Nice to have
• nice catchy looking title

```html
<!DOCTYPE html>
<html lang="en">
<head>
<meta charset="utf-8">
<title>The Velvet Ibiza Getaway – Flyer</title>
<link href="https://fonts.googleapis.com/css2?family=Archivo+Black&family=Oswald:wght@500;600&family=Poppins:wght@400;500;600&family=Russo+One&family=Yellowtail&display=swap" rel="stylesheet">
<style>
  :root{
    --page:#e9e9ec;
    --night:#070a26;
    --deep:#120b3d;
    --violet:#5a1fa8;
    --pink:#ff1f9b;
    --magenta:#e4128c;
    --cyan:#27e0f2;
    --cyan-dark:#0b7fb0;
    --orange:#ff8a1c;
    --white:#ffffff;
    --dim:#c9c6e6;
  }
  *{box-sizing:border-box;margin:0;padding:0}
  html,body{width:1200px;height:3200px;overflow:hidden;background:var(--page)}
  .canvas{position:relative;width:1200px;height:3200px}
  .flyer{
    position:absolute;left:60px;top:835px;width:1080px;height:1530px;overflow:hidden;
    background:
      radial-gradient(ellipse 520px 380px at 15% 52%, rgba(39,224,242,.28), transparent 70%),
      radial-gradient(ellipse 520px 420px at 88% 55%, rgba(255,31,155,.30), transparent 70%),
      radial-gradient(ellipse 700px 500px at 50% 60%, rgba(110,40,200,.45), transparent 75%),
      linear-gradient(180deg, var(--deep) 0%, #1a0f52 40%, var(--night) 78%, var(--night) 100%);
    box-shadow:0 20px 50px rgba(0,0,0,.35);
    font-family:"Poppins",sans-serif;color:var(--white);
  }
  .hero-photo{
    position:absolute;left:0;top:0;width:1080px;height:600px;
    background:
      radial-gradient(ellipse 380px 330px at 48% 55%, rgba(236,228,255,.55), transparent 72%),
      linear-gradient(135deg,#2346c9 0%,#6b3fd0 45%,#8a3cc8 70%,#3b1d8a 100%);
    -webkit-mask-image:linear-gradient(180deg,#000 75%,transparent 100%);
            mask-image:linear-gradient(180deg,#000 75%,transparent 100%);
  }
  .rays{position:absolute;left:0;top:380px;width:1080px;height:500px}
  .title-tag{
    position:absolute;left:225px;top:552px;width:631px;height:88px;border-radius:44px;
    border:3px solid var(--white);padding:7px;background:rgba(10,8,40,.6);
  }
  .title-tag span{
    display:block;height:100%;border-radius:36px;
    background:linear-gradient(90deg,var(--pink) 0%,var(--magenta) 45%,#3a0f4a 100%);
    font-family:"Archivo Black",sans-serif;font-size:50px;letter-spacing:14px;line-height:68px;text-align:center;
    color:var(--white);
  }
  .title-main{
    position:absolute;left:0;top:650px;width:1080px;text-align:center;
    font-family:"Archivo Black",sans-serif;font-size:210px;line-height:1;letter-spacing:-4px;
    background:linear-gradient(180deg,#5ff2ff 0%,var(--cyan) 45%,var(--cyan-dark) 100%);
    -webkit-background-clip:text;background-clip:text;color:transparent;
    filter:drop-shadow(6px 6px 0 var(--pink)) drop-shadow(0 0 18px rgba(39,224,242,.4));
    transform:scaleX(1.05);
  }
  .title-script{
    position:absolute;left:0;top:820px;width:1080px;text-align:center;
    font-family:"Yellowtail",cursive;font-size:150px;line-height:1;color:var(--white);
    text-shadow:4px 4px 0 var(--magenta),0 0 20px rgba(255,31,155,.6);transform:rotate(-4deg);
  }
  .dates{
    position:absolute;left:0;top:1030px;width:1080px;text-align:center;
    font-family:"Oswald",sans-serif;font-weight:600;font-size:60px;line-height:72px;transform:scaleY(1.05);
  }
  .dates .pink{color:var(--pink)} .dates .cyan{color:var(--cyan)}
  .dates sup{font-size:30px;vertical-align:28px}
  .rule{position:absolute;left:175px;width:730px;border-top:2px dotted rgba(255,255,255,.45)}
  .djs{
    position:absolute;left:0;top:1116px;width:1080px;text-align:center;
    font-family:"Russo One",sans-serif;font-size:56px;line-height:62px;letter-spacing:2px;
  }
  .blurb{position:absolute;left:0;top:1180px;width:1080px;text-align:center;font-size:21px;line-height:27px}
  .blurb b{color:var(--cyan);font-weight:600}
  .stats{position:absolute;left:60px;top:1262px;width:960px;display:flex;justify-content:space-between;align-items:center}
  .stat{display:flex;align-items:center;gap:8px;padding-right:14px;border-right:2px solid rgba(255,255,255,.35)}
  .stat:last-child{border-right:0;padding-right:0}
  .stat .num{font-family:"Poppins",sans-serif;font-weight:500;font-size:48px;line-height:50px;color:var(--orange)}
  .stat .label{font-size:16px;line-height:19px;font-weight:500;text-transform:uppercase}
  .perks{position:absolute;left:63px;top:1340px;width:954px;display:flex;justify-content:space-between}
  .perk{border:2px solid var(--pink);border-radius:10px;height:36px;padding:0 14px;font-size:15.5px;font-weight:500;line-height:32px;text-transform:uppercase;white-space:nowrap}
  .price{position:absolute;left:125px;top:1388px}
  .price .lead{font-size:22px;font-weight:500;color:var(--pink);line-height:24px}
  .price .amount{font-family:"Poppins",sans-serif;font-weight:600;font-size:80px;line-height:76px;color:var(--cyan);letter-spacing:-1px}
  .price .saving{position:absolute;left:190px;top:34px;width:240px;font-size:17px;line-height:21px;font-weight:500;text-transform:uppercase}
  .divider{position:absolute;left:578px;top:1398px;width:3px;height:80px;background:var(--orange)}
  .tickets{position:absolute;left:608px;top:1400px}
  .tickets .head{font-size:22px;font-weight:500;line-height:26px;text-transform:uppercase}
  .sellers{display:flex;align-items:center;gap:24px;margin-top:12px}
  .seller{display:flex;align-items:center;gap:8px;font-size:28px;font-weight:600;line-height:32px;color:var(--white)}
  .seller .mark{width:18px;height:18px;background:var(--orange)}
</style>
</head>
<body>
<div class="canvas">
  <article class="flyer">
    <div class="hero-photo" role="img" aria-label="Photo of the two DJs in white t-shirts posing at the decks, blue and purple stage lighting"></div>

    <svg class="rays" viewBox="0 0 1080 500" aria-hidden="true">
      <g stroke-width="3" fill="none" opacity=".7">
        <line x1="0" y1="250" x2="260" y2="300" stroke="#27e0f2"/>
        <line x1="0" y1="300" x2="260" y2="310" stroke="#27e0f2"/>
        <line x1="0" y1="360" x2="260" y2="320" stroke="#27e0f2"/>
        <line x1="1080" y1="250" x2="820" y2="300" stroke="#ff1f9b"/>
        <line x1="1080" y1="300" x2="820" y2="310" stroke="#ff1f9b"/>
        <line x1="1080" y1="360" x2="820" y2="320" stroke="#ff1f9b"/>
      </g>
    </svg>

    <div class="title-tag"><span>THE VELVET</span></div>
    <h1 class="title-main">IBIZA</h1>
    <div class="title-script">Getaway</div>

    <p class="dates">
      <span class="pink">FRIDAY</span> <span class="cyan">14<sup>TH</sup> JULY</span> TO
      <span class="pink">MONDAY</span> <span class="cyan">17<sup>TH</sup> JULY</span>
    </p>
    <div class="rule" style="top:1112px"></div>
    <h2 class="djs">DJ KORVEX &amp; DJ TAMBLIN</h2>
    <p class="blurb">brings together a jam-packed weekend schedule full<br>of the best urban parties <b>in Ibiza</b></p>
    <div class="rule" style="top:1246px"></div>

    <ul class="stats">
      <li class="stat"><span class="num">4</span><span class="label">Nights of<br>Entertainment</span></li>
      <li class="stat"><span class="num">6</span><span class="label">Parties<br>in total</span></li>
      <li class="stat"><span class="num">1</span><span class="label">Boat<br>Party</span></li>
      <li class="stat"><span class="num">1</span><span class="label">Pool<br>Party</span></li>
      <li class="stat"><span class="num">2</span><span class="label">Superclub<br>Parties</span></li>
      <li class="stat"><span class="num">1</span><span class="label">Indoor<br>Water Party</span></li>
    </ul>

    <ul class="perks">
      <li class="perk">Bottomless drinks (boat party only)</li>
      <li class="perk">An unbelievable experience</li>
      <li class="perk">1 unbeatable price</li>
    </ul>

    <div class="price">
      <p class="lead">ALL THIS FOR</p>
      <p class="amount">140€</p>
      <p class="saving">(You save 50€ when you book with us)</p>
    </div>
    <div class="divider"></div>
    <div class="tickets">
      <p class="head">Tickets avaialble from</p>
      <div class="sellers">
        <span class="seller">Queldrix</span>
        <span class="seller"><span class="mark"></span>Ticketmoor</span>
      </div>
    </div>
  </article>
</div>
</body>
</html>
```